BOLD & MINIMALIST DESIGN NEEDED

We want a very bold but minimalistic business card design that is impactful and utilizes both sides of the business card. Our current logo is included for your use.

We want bold fonts and good use of negative space. We don't want the logo to overpower the design.

Target Market(s)

Professionals who are building new commercial buildings.

Industry/Entity Type

Construction

Contact Information for Business Card

Name, Title, email, office phone, cell phone, website

Font styles to use
Serif
Sans Serif

Requirements
Must have
• Bold design!

```html
<!DOCTYPE html>
<html lang="en">
<head>
<meta charset="utf-8">
<title>Crestmark Design + Build — Business Card</title>
<link rel="stylesheet" href="https://fonts.googleapis.com/css2?family=Montserrat:wght@400;500;800&display=swap">
<style>
  :root {
    --bg: #1c1c1c;
    --card-black: #0b0c0e;
    --card-white: #ffffff;
    --green: #7dc42a;
    --green-deep: #2d4216;
    --text-light: #f4f2ef;
    --text-dark: #111111;
  }
  * { margin: 0; padding: 0; box-sizing: border-box; }
  html, body { width: 1200px; height: 1015px; overflow: hidden; }
  body {
    background: var(--bg);
    font-family: "Montserrat", sans-serif;
    position: relative;
  }
  .card {
    position: absolute;
    width: 560px;
    height: 320px;
    overflow: hidden;
    box-shadow: 0 18px 40px rgba(0,0,0,.6);
  }
  .card-front {
    left: 70px; top: 110px;
    background: radial-gradient(ellipse 70% 80% at 100% 0%, var(--green-deep) 0%, var(--card-black) 70%);
  }
  .card-back {
    left: 570px; top: 585px;
    background: var(--card-white);
  }
  .wordmark {
    position: absolute;
    left: 0; right: 0;
    display: flex;
    align-items: center;
    justify-content: center;
    gap: 14px;
  }
  .wordmark-square {
    width: 30px; height: 30px;
    background: var(--green);
    flex: none;
  }
  .wordmark-text {
    font-weight: 800;
    text-transform: uppercase;
    line-height: 1;
    letter-spacing: .02em;
  }
  .wordmark-text .name { display: block; font-size: 42px; }
  .wordmark-text .tagline { display: block; font-size: 15px; letter-spacing: .42em; margin-top: 6px; }
  .card-front .wordmark { top: 118px; }
  .card-front .wordmark-text { color: var(--text-light); }
  .card-back .wordmark { top: 36px; }
  .card-back .wordmark-text { color: var(--text-dark); }
  .card-back .wordmark-text .name { font-size: 34px; }
  .card-back .wordmark-text .tagline { font-size: 12px; }
  .back-band { position: absolute; left: 0; top: 0; width: 560px; height: 320px; }
  .contact {
    position: absolute;
    left: 0; right: 0; bottom: 0;
    height: 150px;
    color: var(--text-light);
  }
  .person { position: absolute; left: 200px; top: 38px; text-align: right; width: 150px; }
  .person-name { color: var(--green); font-weight: 800; font-size: 17px; text-transform: uppercase; }
  .person-title { font-size: 10px; font-weight: 500; text-transform: uppercase; letter-spacing: .02em; }
  .phones { position: absolute; left: 150px; top: 84px; }
  .web { position: absolute; left: 380px; top: 38px; }
  .contact-line {
    display: flex; align-items: center; gap: 8px;
    font-size: 13px; line-height: 24px;
  }
  .phones .contact-line { color: var(--green); font-size: 16px; flex-direction: row-reverse; justify-content: flex-end; }
  .icon { width: 16px; height: 16px; flex: none; }
  .divider {
    position: absolute; left: 366px; top: 40px;
    width: 1px; height: 52px; background: var(--green);
  }
</style>
</head>
<body>
  <section class="card card-front" aria-label="Card front">
    <div class="wordmark">
      <span class="wordmark-square"></span>
      <span class="wordmark-text"><span class="name">Crestmark</span><span class="tagline">Design + Build</span></span>
    </div>
  </section>

  <section class="card card-back" aria-label="Card back">
    <svg class="back-band" viewBox="0 0 560 320" aria-hidden="true">
      <path d="M0 320 L60 320 C150 200 330 110 560 90 L560 320 Z" fill="var(--card-black)"/>
      <path d="M170 215 C260 150 360 105 480 88 C370 110 270 155 170 215 Z" fill="var(--green)"/>
    </svg>

    <div class="wordmark">
      <span class="wordmark-square"></span>
      <span class="wordmark-text"><span class="name">Crestmark</span><span class="tagline">Design + Build</span></span>
    </div>

    <div class="contact">
      <div class="person">
        <div class="person-name">Daniel Marsh</div>
        <div class="person-title">Managing Director</div>
      </div>
      <div class="phones">
        <div class="contact-line">
          <svg class="icon" viewBox="0 0 16 16"><rect x=".5" y=".5" width="15" height="15" rx="2" fill="none" stroke="var(--green)"/><path d="M5 4 l2 2 -1 1 c.5 1.2 1.5 2.2 2.7 2.7 l1-1 2 2 -1.2 1.2 C7 11.5 4.5 9 3.8 5.2Z" fill="var(--green)"/></svg>
          <span>044-555 010 200</span>
        </div>
        <div class="contact-line">
          <svg class="icon" viewBox="0 0 16 16"><rect x=".5" y=".5" width="15" height="15" rx="2" fill="none" stroke="var(--green)"/><rect x="5" y="3.5" width="6" height="9" rx="1" fill="none" stroke="var(--green)"/></svg>
          <span>044-555 010 201</span>
        </div>
      </div>
      <span class="divider"></span>
      <div class="web">
        <div class="contact-line">
          <svg class="icon" viewBox="0 0 16 16"><rect x=".5" y=".5" width="15" height="15" rx="2" fill="none" stroke="var(--green)"/><rect x="3.5" y="5" width="9" height="6" fill="none" stroke="var(--green)"/><path d="M3.5 5 L8 8.5 12.5 5" fill="none" stroke="var(--green)"/></svg>
          <span>hello@crestmark.com</span>
        </div>
        <div class="contact-line">
          <svg class="icon" viewBox="0 0 16 16"><rect x=".5" y=".5" width="15" height="15" rx="2" fill="none" stroke="var(--green)"/><circle cx="8" cy="8" r="4.5" fill="none" stroke="var(--green)"/><path d="M3.5 8 H12.5 M8 3.5 C6 6 6 10 8 12.5 M8 3.5 C10 6 10 10 8 12.5" fill="none" stroke="var(--green)"/></svg>
          <span>www.crestmark.com</span>
        </div>
      </div>
    </div>
  </section>
</body>
</html>
```